Coralbend Pastoral Traders Business Cards

We require business cards revamped with our logo. A few details we would like to use.

1. Round Edges
2. Our logo over the top of a wagyu cattle background photo on one side of the card

Other side of the card has the below details.

1. Person Name (First & Last)
2. Job Position
3. Mobile Number
4. Email Address
5. Website Address

Simple & Neat.

Target Market(s)

Sales

Industry/Entity Type

Agriculture

Contact Information for Business Card

CORALBEND PASTORAL TRADERS

Colors

Designer to choose colors to be used in the design.

Requirements
Must have
• Company Logo

```html
<!DOCTYPE html>
<html lang="en">
<head>
<meta charset="utf-8">
<title>Coralbend Pastoral Traders – Business Card</title>
<link href="https://fonts.googleapis.com/css2?family=Montserrat:wght@500;600;700&display=swap" rel="stylesheet">
<style>
  :root {
    --page: #ffffff;
    --card: #ececec;
    --ink: #1f1f1f;
    --ink-soft: #333333;
    --rule: #d8d8d8;
    --pink: #ff2a7a;
    --icon-pink: #e0357a;
    --blue: #0a8fe8;
    --sky: #7fbbe2;
    --yellow: #ffe014;
  }
  * { margin: 0; padding: 0; box-sizing: border-box; }
  html, body {
    width: 960px; height: 1200px; overflow: hidden;
    background: var(--page);
    font-family: "Montserrat", Arial, sans-serif;
    color: var(--ink);
  }
  .sheet { position: relative; width: 960px; height: 1200px; }
  .side-label {
    position: absolute; left: 0; width: 960px; text-align: center;
    font-size: 29px; font-weight: 600; letter-spacing: 0.5px; color: #111;
  }
  .side-label--front { top: 44px; }
  .side-label--back { top: 607px; }
  .card {
    position: absolute; left: 68px; width: 824px; height: 464px;
    background: var(--card); border-radius: 19px; overflow: hidden;
  }
  .card--front { top: 96px; }
  .card--back { top: 663px; left: 67px; }

  .colour-field { position: absolute; top: 0; height: 330px; }
  .colour-field--front {
    right: 0; width: 484px;
    background: linear-gradient(to bottom left, var(--pink) 0%, var(--yellow) 40%, var(--sky) 70%, var(--card) 100%);
  }
  .colour-field--back {
    left: 0; width: 420px;
    background: linear-gradient(to bottom right, var(--pink) 0%, var(--yellow) 40%, var(--sky) 70%, var(--card) 100%);
  }

  .brand { position: absolute; display: flex; align-items: center; }
  .brand__dot { border-radius: 50%; background: var(--blue); flex: none; }
  .brand__name { color: var(--pink); font-weight: 700; line-height: 1.05; }
  .brand--front { left: 24px; top: 30px; gap: 14px; }
  .brand--front .brand__dot { width: 58px; height: 58px; }
  .brand--front .brand__name { font-size: 22px; }
  .brand--back { right: 23px; top: 16px; gap: 8px; }
  .brand--back .brand__dot { width: 26px; height: 26px; }
  .brand--back .brand__name { font-size: 11px; text-align: left; }

  .tagline {
    position: absolute; left: 160px; top: 366px; width: 504px; height: 42px;
    border-top: 1.5px solid var(--ink); border-bottom: 1.5px solid var(--ink);
    display: flex; align-items: center; justify-content: center;
    font-size: 21.5px; font-weight: 700; color: #222; letter-spacing: 0.3px;
  }

  .person { position: absolute; left: 47px; width: 280px; top: 355px; text-align: center; }
  .person__name { font-size: 30px; font-weight: 700; color: var(--ink); letter-spacing: 0.3px; }
  .person__role { font-size: 14px; font-weight: 700; color: #2b2b2b; margin-top: 2px; letter-spacing: 0.4px; }

  .contacts { position: absolute; left: 429px; width: 372px; top: 254px; list-style: none; }
  .contact {
    display: flex; align-items: center; justify-content: flex-end; gap: 19px;
    height: 65px; font-size: 24.5px; font-weight: 500; color: var(--ink-soft);
  }
  .contact + .contact { border-top: 1.5px solid var(--rule); }
  .contact:first-child { height: 64px; }
  .contact__icon {
    width: 28px; height: 28px; background: var(--icon-pink);
    display: flex; align-items: center; justify-content: center; flex: none;
  }
  .contact__icon svg { width: 17px; height: 17px; }
</style>
</head>
<body>
<main class="sheet">
  <h2 class="side-label side-label--front">FRONT SIDE</h2>
  <section class="card card--front" aria-label="Business card front">
    <div class="colour-field colour-field--front" role="img" aria-label="Wagyu cattle background photo area"></div>
    <div class="brand brand--front">
      <span class="brand__dot"></span>
      <span class="brand__name">CORALBEND<br>PASTORAL<br>TRADERS</span>
    </div>
    <p class="tagline">BEEF TRADER AND WAGYU EXPORTER</p>
  </section>

  <h2 class="side-label side-label--back">BACK SIDE</h2>
  <section class="card card--back" aria-label="Business card back">
    <div class="colour-field colour-field--back" role="img" aria-label="Abstract colour decoration in pink, yellow and blue"></div>
    <div class="brand brand--back">
      <span class="brand__dot"></span>
      <span class="brand__name">CORALBEND<br>PASTORAL<br>TRADERS</span>
    </div>
    <div class="person">
      <p class="person__name">PERSON NAME</p>
      <p class="person__role">JOB POSITION</p>
    </div>
    <ul class="contacts">
      <li class="contact">
        <span class="contact__text">111-222-3333</span>
        <span class="contact__icon">
          <svg viewBox="0 0 24 24" aria-hidden="true"><path fill="#fff" d="M6.6 10.8a15.1 15.1 0 0 0 6.6 6.6l2.2-2.2c.3-.3.7-.4 1-.2 1.1.4 2.3.6 3.6.6.6 0 1 .4 1 1V20c0 .6-.4 1-1 1A17 17 0 0 1 3 4c0-.6.4-1 1-1h3.5c.6 0 1 .4 1 1 0 1.3.2 2.5.6 3.6.1.3 0 .7-.2 1z"/></svg>
        </span>
      </li>
      <li class="contact">
        <span class="contact__text">Email Address</span>
        <span class="contact__icon">
          <svg viewBox="0 0 24 24" aria-hidden="true"><rect x="3" y="5.5" width="18" height="13" fill="none" stroke="#fff" stroke-width="1.6"/><path d="M3 6l9 7 9-7M3 18l7-6M21 18l-7-6" fill="none" stroke="#fff" stroke-width="1.4"/></svg>
        </span>
      </li>
      <li class="contact">
        <span class="contact__text">Website Address</span>
        <span class="contact__icon">
          <svg viewBox="0 0 24 24" aria-hidden="true"><g fill="none" stroke="#fff" stroke-width="1.5"><circle cx="12" cy="12" r="9"/><ellipse cx="12" cy="12" rx="4" ry="9"/><path d="M3 12h18M4.5 7.5h15M4.5 16.5h15"/></g></svg>
        </span>
      </li>
    </ul>
  </section>
</main>
</body>
</html>
```